Talvero Engineering & Management Services Website

A professional website design that outlines Engineering and Management Services. The website is to be colour coordinated with the current logo (see attached). The webpage needs to be compatible with Wordpress to allow for easy changes to be made to the website for the user.
Required tabs for the page include:
- Civil Engineering
- Structural Engineering
- Project Management
- Business Management
- Project Controls
- Drafting
- Contact Us

Clean and efficient website that matches the services provided by the business.

Target Market(s)

New Customers to a very competitive market

Industry/Entity Type

Engineering

Number of Pages Required

5+ page

Requirements
Must have
• Clean with large stock photos

```html
<!DOCTYPE html>
<html lang="en">
<head>
<meta charset="utf-8">
<title>Talvero Engineering & Management Services</title>
<link href="https://fonts.googleapis.com/css2?family=Open+Sans:wght@400;600;700&family=Oswald:wght@400;500;700&display=swap" rel="stylesheet">
<style>
:root{
  --orange:#f47b20;
  --ink:#333;
  --text:#666;
  --muted:#999;
  --line:#ddd;
  --panel:#ececec;
  --dark:#6b6b6b;
  --darker:#4e4e4e;
  --footer:#e2e2e2;
  --white:#fff;
}
*{box-sizing:border-box;margin:0;padding:0}
html,body{width:1200px;height:2484px;overflow:hidden}
body{font-family:"Open Sans",Arial,sans-serif;color:var(--text);background:var(--white);font-size:14px}
.wrap{width:1080px;margin:0 auto;position:relative}
h1,h2,h3,h4,.nav a,.label{font-family:"Oswald",Arial,sans-serif}

.site-header{height:112px}
.site-header .wrap{display:flex;justify-content:space-between;align-items:center;height:112px}
.brand{display:flex;align-items:center;gap:12px}
.brand-mark{width:40px;height:40px;background:var(--orange)}
.brand-name{font-family:"Oswald",sans-serif;font-weight:700;font-size:34px;color:var(--ink);line-height:1}
.brand-sub{font-family:"Oswald",sans-serif;font-size:11px;color:var(--orange);letter-spacing:1px;text-transform:uppercase}
.header-right{display:flex;align-items:center;gap:22px}
.socials{display:flex;gap:8px}
.socials span{width:28px;height:28px;border-radius:50%;background:#c8c8c8}
.call small{display:block;font-size:12px;color:var(--text);text-align:right}
.call strong{font-family:"Oswald",sans-serif;font-size:24px;color:var(--orange);font-weight:500}

.nav{height:48px;border-top:1px solid var(--line);border-bottom:1px solid var(--line)}
.nav .wrap{display:flex;height:100%}
.nav a{flex:auto;display:flex;align-items:center;justify-content:center;font-size:14px;color:var(--ink);text-decoration:none;text-transform:uppercase;border-right:1px solid var(--line)}
.nav a:first-child{border-left:1px solid var(--line)}
.nav a.active{background:var(--orange);color:var(--white)}

.hero{height:580px;position:relative;background:linear-gradient(180deg,#b9c6d0 0%,#8e9ba4 55%,#56606a 100%);text-align:center}
.hero h1{position:absolute;top:200px;left:0;right:0;font-size:64px;letter-spacing:14px;color:var(--white);font-weight:500}
.hero p{position:absolute;top:290px;left:0;right:0;font-size:20px;color:var(--white);font-weight:600}
.btn{display:inline-block;background:var(--orange);color:var(--white);font-family:"Oswald",sans-serif;font-size:18px;padding:10px 32px;text-transform:uppercase}
.hero .btn{position:absolute;top:340px;left:50%;transform:translateX(-50%)}
.dots{position:absolute;bottom:26px;left:0;right:0;display:flex;justify-content:center;gap:8px}
.dots i{width:14px;height:14px;border-radius:50%;background:rgba(255,255,255,.6)}
.dots i:first-child{background:var(--orange)}

.welcome{height:360px;padding-top:40px}
.welcome .wrap{display:flex;gap:40px}
.welcome-text{flex:1}
.welcome h2{font-size:24px;color:var(--ink);font-weight:500;line-height:1.2;margin-bottom:22px}
.welcome p{font-size:13px;line-height:1.75;margin-bottom:18px}
.video{width:340px}
.video h3{font-size:24px;color:var(--ink);font-weight:500;margin-bottom:16px}
.video-frame{height:180px;background:linear-gradient(135deg,#6d7f8c,#c2a27a);position:relative}
.video-frame svg{position:absolute;left:140px;top:60px}

.services{background:var(--panel);height:700px;padding-top:50px}
.services h2{text-align:center;font-size:28px;color:var(--ink);font-weight:500;margin-bottom:36px}
.grid{display:grid;grid-template-columns:repeat(3,1fr);gap:40px 50px}
.card .photo{height:170px}
.card .label{background:var(--white);height:70px;display:flex;align-items:center;justify-content:center;font-size:18px;color:var(--ink);text-transform:uppercase;box-shadow:0 2px 4px rgba(0,0,0,.08)}
.p1{background:linear-gradient(135deg,#8fa3b3,#d59a4a)}
.p2{background:linear-gradient(135deg,#dfe4ea,#8b99a8)}
.p3{background:linear-gradient(135deg,#b7c8d8,#5f6f80)}
.p4{background:linear-gradient(135deg,#c9b9a8,#7d8c99)}
.p5{background:linear-gradient(135deg,#e0dccf,#8e8a80)}
.p6{background:linear-gradient(135deg,#a6b9cc,#4a5966)}

.feeds{height:360px;padding-top:40px}
.feeds .wrap{display:grid;grid-template-columns:repeat(3,1fr);gap:50px}
.feed h3{font-size:20px;color:var(--ink);font-weight:500;border-bottom:3px solid var(--ink);padding-bottom:8px;margin-bottom:14px}
.item{display:flex;justify-content:space-between;align-items:center;gap:10px;border-bottom:1px solid var(--line);padding:6px 0 10px}
.item div{font-size:12px;line-height:1.5}
.item b{display:block;color:var(--orange);font-weight:400}
.item span{color:var(--orange);font-size:22px}
.more{display:block;margin-top:12px;font-size:13px;color:var(--orange);font-weight:600}

.ask{background:var(--dark);height:92px;color:var(--white)}
.ask .wrap{display:flex;align-items:center;height:100%;gap:60px}
.ask h3{font-size:26px;font-weight:500;line-height:1;text-transform:uppercase}
.ask-item{display:flex;align-items:center;gap:12px;font-size:12px;text-transform:uppercase;line-height:1.4}

.footer{background:var(--footer);height:188px;padding-top:20px}
.footer .wrap{display:grid;grid-template-columns:repeat(4,1fr);gap:40px}
.footer h4{font-size:13px;color:var(--ink);font-weight:500;text-transform:uppercase;margin-bottom:14px}
.footer p,.footer li{font-size:12px;line-height:1.6;list-style:none}
.footer input{display:block;width:200px;height:28px;border:1px solid var(--line);margin:10px 0 8px;font-size:11px;padding:0 8px}
.footer .btn{font-size:12px;padding:6px 16px}
.footer .socials span{width:32px;height:32px;background:#999}

.bottom{background:var(--darker);height:44px;color:#ccc;font-size:12px;text-align:center;line-height:44px}
</style>
</head>
<body>
<header class="site-header">
  <div class="wrap">
    <div class="brand">
      <span class="brand-mark"></span>
      <div>
        <div class="brand-name">TALVERO</div>
        <div class="brand-sub">Engineering &amp; Management Services</div>
      </div>
    </div>
    <div class="header-right">
      <div class="socials"><span></span><span></span><span></span></div>
      <div class="call"><small>Questions? Call</small><strong>1-800-555-0147</strong></div>
    </div>
  </div>
</header>

<nav class="nav">
  <div class="wrap">
    <a class="active">Home</a><a>Civil Engineering</a><a>Structural Engineering</a><a>Project Management</a><a>Business Management</a><a>Project Controls</a><a>Drafting</a><a>Contact Us</a>
  </div>
</nav>

<section class="hero" role="img" aria-label="Engineer in a hard hat reviewing plans at an industrial port">
  <h1>LOREM IPSUM DOLOR SIT AMET</h1>
  <p>Sed ut perspiciatis unde omnis iste natus error sit voluptatem accusantium</p>
  <span class="btn">Learn More</span>
  <div class="dots"><i></i><i></i><i></i><i></i></div>
</section>

<section class="welcome">
  <div class="wrap">
    <div class="welcome-text">
      <h2>Welcome to<br>Talvero Engineering and Management Services</h2>
      <p>Lorem ipsum dolor sit amet, consectetur adipiscing elit, sed do eiusmod tempor incididunt ut labore et dolore magna aliqua. Ut enim ad minim veniam, quis nostrud exercitation ullamco laboris nisi ut aliquip ex ea commodo consequat. Duis aute irure dolor in reprehenderit in voluptate velit esse cillum dolore eu fugiat nulla pariatur. Excepteur sint occaecat cupidatat non proident, sunt in culpa qui officia deserunt mollit anim id est laborum.</p>
      <p>Sed ut perspiciatis unde omnis iste natus error sit voluptatem accusantium doloremque laudantium, totam rem aperiam, eaque ipsa quae ab illo inventore veritatis et quasi architecto beatae vitae dicta sunt explicabo.</p>
    </div>
    <div class="video">
      <h3>Our Video</h3>
      <div class="video-frame" role="img" aria-label="Video still of engineers on a construction site">
        <svg width="60" height="60" viewBox="0 0 60 60"><rect x="4" y="12" width="52" height="36" rx="8" fill="#222"/><path d="M25 21 L38 30 L25 39Z" fill="#fff"/></svg>
      </div>
    </div>
  </div>
</section>

<section class="services">
  <div class="wrap">
    <h2>Our Services</h2>
    <div class="grid">
      <div class="card"><div class="photo p1" role="img" aria-label="Civil engineers on site"></div><div class="label">Civil Engineering</div></div>
      <div class="card"><div class="photo p2" role="img" aria-label="Structural framework detail"></div><div class="label">Structural Engineering</div></div>
      <div class="card"><div class="photo p3" role="img" aria-label="Project planning meeting"></div><div class="label">Project Management</div></div>
      <div class="card"><div class="photo p4" role="img" aria-label="Business team at a table"></div><div class="label">Business Management</div></div>
      <div class="card"><div class="photo p5" role="img" aria-label="Charts and reports on a desk"></div><div class="label">Project Controls</div></div>
      <div class="card"><div class="photo p6" role="img" aria-label="Technical drafting on screen"></div><div class="label">Drafting</div></div>
    </div>
  </div>
</section>

<section class="feeds">
  <div class="wrap">
    <div class="feed"><h3>NEWS</h3>
      <div class="item"><div><b>2 September 2015</b>Lorem ipsum dolor sit amet, consectetur adipiscing elit</div><span>›</span></div>
      <div class="item"><div><b>2 September 2015</b>Lorem ipsum dolor sit amet, consectetur adipiscing elit</div><span>›</span></div>
      <div class="item"><div><b>2 September 2015</b>Lorem ipsum dolor sit amet, consectetur adipiscing elit</div><span>›</span></div>
      <span class="more">More News »</span></div>
    <div class="feed"><h3>EVENTS</h3>
      <div class="item"><div><b>2 September 2015</b>Lorem ipsum dolor sit amet, consectetur adipiscing elit</div><span>›</span></div>
      <div class="item"><div><b>2 September 2015</b>Lorem ipsum dolor sit amet, consectetur adipiscing elit</div><span>›</span></div>
      <div class="item"><div><b>2 September 2015</b>Lorem ipsum dolor sit amet, consectetur adipiscing elit</div><span>›</span></div>
      <span class="more">More Events »</span></div>
    <div class="feed"><h3>TWITTER</h3>
      <div class="item"><div><b>2 September 2015</b>@talvero_ems Sed ut perspiciatis unde omnis iste natus error</div><span>›</span></div>
      <div class="item"><div><b>2 September 2015</b>@talvero_ems Sed ut perspiciatis unde omnis iste natus error</div><span>›</span></div>
      <div class="item"><div><b>2 September 2015</b>@talvero_ems Sed ut perspiciatis unde omnis iste natus error</div><span>›</span></div>
      <span class="more">More Twitter »</span></div>
  </div>
</section>

<section class="ask">
  <div class="wrap">
    <h3>Have<br>Questions?</h3>
    <div class="ask-item"><svg width="30" height="30" viewBox="0 0 24 24"><path d="M6.6 10.8a15 15 0 006.6 6.6l2.2-2.2a1 1 0 011-.25 11 11 0 003.6.6 1 1 0 011 1V20a1 1 0 01-1 1A17 17 0 013 4a1 1 0 011-1h3.5a1 1 0 011 1 11 11 0 00.6 3.6 1 1 0 01-.25 1z" fill="#fff"/></svg><span>Call Us<br>(31) 5550 1928</span></div>
    <div class="ask-item"><svg width="30" height="30" viewBox="0 0 24 24"><rect x="2" y="5" width="20" height="14" fill="none" stroke="#fff" stroke-width="2"/><path d="M2 6l10 7 10-7" fill="none" stroke="#fff" stroke-width="2"/></svg><span>Send Us<br>An Email</span></div>
    <div class="ask-item"><svg width="30" height="30" viewBox="0 0 24 24"><path d="M12 2a7 7 0 00-7 7c0 5 7 13 7 13s7-8 7-13a7 7 0 00-7-7zm0 9.5A2.5 2.5 0 1112 6.5a2.5 2.5 0 010 5z" fill="#fff"/></svg><span>Find A<br>Local Office</span></div>
    <div class="ask-item"><svg width="30" height="30" viewBox="0 0 24 24"><circle cx="12" cy="12" r="10" fill="none" stroke="#fff" stroke-width="2"/><text x="12" y="17" text-anchor="middle" font-size="14" fill="#fff" font-family="Arial">?</text></svg><span>Read The<br>FAQs</span></div>
  </div>
</section>

<footer class="footer">
  <div class="wrap">
    <div><h4>Contact Us</h4><p>120 Larch Street Suite 400<br>Harbour Point, NSW 2000<br>(31) 5550 1928</p></div>
    <div><h4>Subscribe Our Newsletter</h4><p>Lorem ipsum dolor sit amet consectetur adipiscing elit sed do.</p><input value="Enter Email" readonly><span class="btn">Subscribe</span></div>
    <div><h4>Quick Links</h4><ul><li>Civil Engineering</li><li>Structural Engineering</li><li>Project Management</li><li>Business Management</li><li>Project Controls</li><li>Drafting</li></ul></div>
    <div><h4>Connect With Us</h4><div class="socials"><span></span><span></span><span></span></div></div>
  </div>
</footer>

<div class="bottom">© 2015 Talvero. All Rights Reserved. &nbsp;|&nbsp; Terms and Conditions &nbsp;|&nbsp; Privacy Policy &nbsp;|&nbsp; Terms of Use</div>
</body>
</html>
```